UNDER ONE [BRIGHT] LANTERN, Shape your path

We are looking for a cover refresh of an existing bestselling book that is going into 3rd edition print this year.
The book is an inspirational as well as educational book that has become recognized as one of the most comprehensive, actionable, personal and financial planning resources available today for families, individuals and business owners alike.
Comprised of three true stories of loss, learning to live and love again and a 30 page checklist at the back of the book it contains tips and strategies for everyone to help them to get their personal and financial lives in order while they can.
The cover must have the following:
1. Appeal to a broad audience/both personal and corporate
2. Include Mira Tollenkamp Bestselling Author
3. Include introduction of a new Afterword
4. 3rd Edition
5. Colors to remain the same – red, black and white
6. The title must remain in caps and the word [BRIGHT] must have the brackets around it
We have also added a current copy of the second edition to help you. For your information our website is www.thetollenkampcircle.example
Reason: We have narrowed it down to our top 3 designs. We are submitting the covers to our community for them to pick the top cover. Good luck to everyone

```html
<!DOCTYPE html>
<html lang="en">
<head>
<meta charset="utf-8">
<title>Under One [Bright] Lantern – Cover Wrap</title>
<link rel="stylesheet" href="https://fonts.googleapis.com/css2?family=Anton&family=EB+Garamond:wght@400;500&family=Kaushan+Script&display=swap">
<style>
  :root {
    --paper: #ffffff;
    --silver: #bfbfbf;
    --glow: #ffffff;
    --red: #c20e1d;
    --ink: #232323;
    --spine: #000000;
    --grey-text: #8c8c8c;
    --body-text: #1e1e1e;
  }
  html, body {
    margin: 0;
    padding: 0;
    width: 1200px;
    height: 1200px;
    overflow: hidden;
    background: var(--paper);
  }
  .canvas {
    position: relative;
    width: 1200px;
    height: 1200px;
    background: var(--paper);
  }
  .back-cover {
    position: absolute;
    left: 78px; top: 250px;
    width: 480px; height: 720px;
    background: radial-gradient(ellipse 300px 420px at 240px 330px, var(--glow) 0%, #f2f2f2 35%, var(--silver) 100%);
  }
  .spine {
    position: absolute;
    left: 558px; top: 250px;
    width: 72px; height: 720px;
    background: var(--spine);
  }
  .front-cover {
    position: absolute;
    left: 630px; top: 250px;
    width: 480px; height: 720px;
    background: radial-gradient(ellipse 330px 420px at 250px 390px, var(--glow) 0%, #f4f4f4 40%, var(--silver) 100%);
  }
  .barcode-space {
    position: absolute;
    left: 300px; top: 580px;
    width: 143px; height: 98px;
    background: var(--paper);
  }
  .blurb {
    position: absolute;
    left: 72px; top: 230px;
    width: 336px;
    margin: 0;
    font-family: "EB Garamond", serif;
    font-size: 13.4px;
    line-height: 18px;
    color: var(--body-text);
    text-align: center;
  }
  .artwork {
    position: absolute;
    left: 0; top: 0;
  }
  .title-condensed { font-family: "Anton", sans-serif; }
  .tagline { font-family: "Kaushan Script", cursive; }
  .serif { font-family: "EB Garamond", serif; }
</style>
</head>
<body>
<div class="canvas">
  <div class="back-cover">
    <p class="blurb">Lorem ipsum dolor sit amet, consectetuer adipiscing elit. Aenean commodo ligula eget dolor. Aenean massa. Cum sociis natoque penatibus et magnis dis parturient montes, nascetur ridiculus mus. Donec quam felis, ultricies nec, pellentesque eu, pretium quis, sem. Nulla consequat massa quis enim. Donec pede justo, fringilla vel, aliquet nec, vulputate eget, arcu. In enim justo, rhoncus ut, imperdiet a, venenatis vitae, justo. Nullam dictum felis eu pede mollis pretium. Integer tincidunt. Cras dapibus. Vivamus elementum semper nisi. Aenean vulputate eleifend tellus. Aenean leo ligula, porttitor eu, consequat vitae, eleifend ac, enim. Aliquam lorem ante, dapibus in, viverra quis, feugiat a, tellus. Phasellus viverra nulla ut metus varius laoreet. Quisque rutrum. Aenean imperdiet. Etiam ultricies nisi vel augue</p>
    <div class="barcode-space"></div>
  </div>
  <div class="spine"></div>
  <div class="front-cover"></div>

  <svg class="artwork" width="1200" height="1200" viewBox="0 0 1200 1200">
    <defs>
      <linearGradient id="penTones" x1="0" y1="0" x2="1" y2="0.6">
        <stop offset="0" stop-color="#1c1c1c" stop-opacity="0.8"/>
        <stop offset="0.28" stop-color="#b58a3c" stop-opacity="0.6"/>
        <stop offset="0.55" stop-color="#555555" stop-opacity="0.2"/>
        <stop offset="1" stop-color="#ffffff" stop-opacity="0"/>
      </linearGradient>
    </defs>

    <!-- Front cover artwork area, kept clear of the subtitle and edition line -->
    <rect class="pen-artwork" x="630" y="658" width="460" height="186" fill="url(#penTones)" role="img" aria-label="Illustration of a gold-nibbed fountain pen with ink drops, trailing a wavy ink line"/>

    <!-- Back cover title -->
    <text class="title-condensed back-title" x="142" y="406" font-size="31" textLength="336" lengthAdjust="spacingAndGlyphs"><tspan fill="var(--red)">UNDER ONE </tspan><tspan fill="var(--ink)">[BRIGHT]</tspan><tspan fill="var(--red)"> LANTERN</tspan></text>

    <!-- Spine -->
    <text class="title-condensed spine-title" transform="translate(578 292) rotate(90)" x="0" y="0" font-size="30" fill="#ffffff" textLength="332" lengthAdjust="spacingAndGlyphs">UNDER ONE [BRIGHT] LANTERN</text>
    <text class="serif spine-author" transform="translate(585 784) rotate(90)" x="0" y="0" font-size="25" fill="#ffffff" textLength="152" lengthAdjust="spacingAndGlyphs">Mira Tollenkamp</text>

    <!-- Front title -->
    <text class="title-condensed front-title-top" x="696" y="352" font-size="86" fill="var(--red)" textLength="344" lengthAdjust="spacingAndGlyphs">UNDER ONE</text>
    <path class="bracket bracket-left" d="M684 342 H652 V478 H684 V464 H668 V356 H684 Z" fill="var(--ink)"/>
    <text class="title-condensed front-title-key" x="688" y="452" font-size="118" fill="var(--ink)" textLength="362" lengthAdjust="spacingAndGlyphs">BRIGHT</text>
    <path class="bracket bracket-right" d="M1054 342 H1086 V478 H1054 V464 H1070 V356 H1054 Z" fill="var(--ink)"/>
    <text class="title-condensed front-title-bottom" x="698" y="532" font-size="86" fill="var(--red)" textLength="340" lengthAdjust="spacingAndGlyphs">LANTERN</text>

    <text class="tagline" x="704" y="598" font-size="52" fill="#111111" textLength="328" lengthAdjust="spacingAndGlyphs">Shape your path</text>
    <text class="serif edition" x="713" y="640" font-size="27" fill="var(--grey-text)" textLength="121" lengthAdjust="spacingAndGlyphs">3rd Edition</text>

    <text class="serif author-label" x="869" y="875" font-size="19" font-weight="500" fill="#111111" text-anchor="middle" letter-spacing="0.5">BESTSELLING AUTHOR</text>
    <text class="serif author-name" x="869" y="929" font-size="46" fill="var(--red)" text-anchor="middle" textLength="320" lengthAdjust="spacingAndGlyphs">Mira Tollenkamp</text>
  </svg>
</div>
</body>
</html>
```